INSTAGRAM STORY FEED FOR LUXURY JEWELRY STORE

For a luxury jewelry retailer. We want to create a set of posts for feed for the post-covid world once we reopen. Our goal is to emphasize the rebirth, the beggining of a new day, with focuses on the REAL important things in life: LOVE (through an engagement rings). LIFE (through baby birth gifts). HAPINESS (through benchmark moments like anniversaries).
Colors must be elegant but happy.
for refference our company Instagram is @vorenti_official so you can have a feel of our brand and product.

Target Market(s)

ENGAGEMENT RINGS. DIAMOND CUSTOMERS. LUXURY RETAIL. LATIN AMERICA.

Industry/Entity Type

Jewelry

Font styles to use
Other font styles liked:
• Our logo uses AUDREY

Requirements
Must have
• THEME MUST BE BASED ON A NEW DAY. ELEGANT COLOR SCHEME, WITH LIGHT COLORS, MUST INCLUDE SEVERAL POSTS FOR INSTAGRAM FEED INCLUDING:
Our goal is to emphasize the rebirth, the beggining of a new day, with focuses on the REAL important things in life: LOVE (through an engagement rings). LIFE (through baby birth gifts). HAPINESS (through benchmark moments like anniversaries).
Nice to have
• CLEAN LOOK. PLEASE VIEW IMAGE EXAMPLES OF THINGS I LIKE.
I HAVE POSTED A “LOVE” SIGN IN IMAGES. It would be nice to make something like that sign, in black font, and white, light grey, or even yellow background, and have a ring or piece of jewelrry balancing or hanging from
One of the letters. Then do something similar with word Life, etc.
Should not have
• NO BLACK. NO DARK COLORS. NOTHING THAT WILL LOOK TACKY.

```html
<!DOCTYPE html>
<html lang="en">
<head>
<meta charset="utf-8">
<title>Vorenti — New Guest Story</title>
<link rel="stylesheet" href="https://fonts.googleapis.com/css2?family=Cinzel:wght@400;600&family=Cormorant+Garamond:wght@500&display=swap">
<style>
  :root {
    --backdrop: #9fd8e6;
    --sky-cream: #fde7c6;
    --blush-light: #f9b8d6;
    --blush: #f39ac6;
    --blush-deep: #ee86bb;
    --gold-light: #f6cf72;
    --gold: #ebb452;
    --gold-deep: #e0a03e;
    --accent-red: #e8392a;
    --ink: #3a3433;
    --white: #ffffff;
  }
  html, body {
    margin: 0;
    padding: 0;
    width: 1200px;
    height: 1040px;
    overflow: hidden;
    background: var(--backdrop);
  }
  .canvas {
    position: relative;
    width: 1200px;
    height: 1040px;
  }
  .story {
    position: absolute;
    left: 324px;
    top: 31px;
    width: 551px;
    height: 978px;
    box-shadow: 0 6px 18px rgba(0, 0, 0, 0.18);
  }
  .brand-name {
    font-family: "Cinzel", serif;
    font-weight: 400;
    font-size: 48px;
    letter-spacing: 16px;
    fill: var(--ink);
  }
  .headline {
    font-family: "Cinzel", serif;
    font-weight: 400;
    font-size: 42px;
    letter-spacing: 2px;
    fill: var(--white);
  }
  .headline--strong {
    font-weight: 600;
  }
  .cta-label {
    font-family: "Cinzel", serif;
    font-size: 21px;
    letter-spacing: 1px;
    fill: var(--white);
  }
  .web-address {
    font-family: "Cormorant Garamond", serif;
    font-weight: 500;
    font-size: 38px;
    fill: var(--ink);
  }
</style>
</head>
<body>
<main class="canvas">
  <svg class="story" viewBox="0 0 588 1043" xmlns="http://www.w3.org/2000/svg">
    <defs>
      <linearGradient id="dawn-photo" x1="0" y1="0" x2="0.3" y2="1">
        <stop offset="0" stop-color="var(--sky-cream)"/>
        <stop offset="0.22" stop-color="var(--blush-light)"/>
        <stop offset="0.6" stop-color="var(--blush)"/>
        <stop offset="1" stop-color="var(--blush-deep)"/>
      </linearGradient>
      <linearGradient id="gold-foil" x1="0" y1="0" x2="1" y2="1">
        <stop offset="0" stop-color="var(--gold-light)"/>
        <stop offset="0.5" stop-color="var(--gold)"/>
        <stop offset="1" stop-color="var(--gold-deep)"/>
      </linearGradient>
    </defs>

    <polygon class="photo-area" points="0,0 588,0 588,640 0,885" fill="url(#dawn-photo)"
             role="img" aria-label="Photo: a newborn's tiny feet cradled in a parent's hands, with a pink sunrise over hills behind"/>
    <polygon class="gold-band" points="0,885 588,640 588,1043 0,1043" fill="url(#gold-foil)"/>
    <line class="accent-stripe" x1="-2" y1="886" x2="590" y2="639" stroke="var(--accent-red)" stroke-width="12"/>

    <text class="brand-name" x="302" y="127" text-anchor="middle">VORENTI</text>

    <rect class="headline-frame" x="44" y="164" width="501" height="215" fill="none" stroke="var(--white)" stroke-width="2"/>
    <text class="headline" x="294" y="232" text-anchor="middle">GET SOMETHING</text>
    <text class="headline" x="294" y="286" text-anchor="middle">SPECIAL FOR THE</text>
    <text class="headline headline--strong" x="294" y="341" text-anchor="middle">NEW GUEST</text>

    <rect class="cta-button" x="202" y="882" width="184" height="37" rx="18.5" fill="var(--accent-red)"/>
    <text class="cta-label" x="294" y="908" text-anchor="middle">SHOP NOW</text>

    <text class="web-address" x="294" y="967" text-anchor="middle">vorenti.com.pa</text>
  </svg>
</main>
</body>
</html>
```